Online Psychology Practice needs business cards.

Online Psychology service needs business cards. Have own logo- please see uploaded. I have other file formats if you need (not sure one needed?)

Details for Business Card:
Helena Marchetti
Clinical Psychologist BPsych, BPsych (Hons), MPsych (Clin), MAPS
T: 0439627015 | F: 08 73615204
E: hello@brightwatertelehealthcounselling.com.au
W: brightwatertelehealthcounselling.com.au

Industry/Entity Type

Health

Contact Information for Business Card

Logo plus details above (couldn't write in this section)

```html
<!DOCTYPE html>
<html lang="en">
<head>
<meta charset="utf-8">
<title>Brightwater Telehealth Counselling – Business Card</title>
<link rel="stylesheet" href="https://fonts.googleapis.com/css2?family=Lato:wght@400;700&display=swap">
<style>
  :root {
    --backdrop: #b5b5b5;
    --card-white: #ffffff;
    --teal-light: #1591a8;
    --teal-deep: #165d87;
    --brand-blue: #1b5a82;
    --brand-teal: #1a88a6;
    --ink: #111111;
    --ink-soft: #222222;
  }
  * { box-sizing: border-box; margin: 0; padding: 0; }
  html, body {
    width: 1048px;
    height: 1200px;
    overflow: hidden;
    background: var(--backdrop);
    font-family: "Lato", Arial, sans-serif;
  }
  .canvas {
    position: relative;
    width: 1048px;
    height: 1200px;
  }
  .card {
    position: absolute;
    left: 138px;
    width: 773px;
    height: 441px;
  }
  .card--front {
    top: 132px;
    background: linear-gradient(150deg, var(--teal-light) 0%, var(--teal-deep) 100%);
    display: flex;
    flex-direction: column;
    align-items: center;
    justify-content: center;
  }
  .card--back {
    top: 626px;
    background: var(--card-white);
  }
  .brand-dot {
    width: 70px;
    height: 70px;
    border-radius: 50%;
  }
  .card--front .brand-dot { background: var(--card-white); margin-bottom: 26px; }
  .brand-name {
    font-weight: 400;
    text-align: center;
    line-height: 1.15;
  }
  .card--front .brand-name {
    color: var(--card-white);
    font-size: 34px;
    letter-spacing: 1px;
  }
  .back-brand {
    position: absolute;
    left: 38px;
    top: 28px;
    width: 220px;
    display: flex;
    flex-direction: column;
    align-items: center;
  }
  .back-brand .brand-dot { background: var(--brand-teal); width: 54px; height: 54px; margin-bottom: 18px; }
  .back-brand .brand-name { color: var(--brand-blue); font-size: 22px; }
  .person {
    position: absolute;
    right: 28px;
    top: 24px;
    text-align: right;
  }
  .person__name {
    font-weight: 700;
    font-size: 46px;
    color: var(--brand-blue);
    line-height: 1.1;
    margin-bottom: 6px;
  }
  .person__credentials {
    font-size: 19.5px;
    color: var(--ink-soft);
    line-height: 25.5px;
  }
  .contact {
    position: absolute;
    left: 34px;
    top: 282px;
    font-size: 27px;
    color: var(--ink);
    line-height: 34px;
    list-style: none;
  }
</style>
</head>
<body>
<main class="canvas">
  <section class="card card--front" aria-label="Card front">
    <span class="brand-dot"></span>
    <p class="brand-name">Brightwater<br>Telehealth Counselling</p>
  </section>

  <section class="card card--back" aria-label="Card back">
    <div class="back-brand">
      <span class="brand-dot"></span>
      <p class="brand-name">Brightwater<br>Telehealth Counselling</p>
    </div>

    <div class="person">
      <h1 class="person__name">Helena Marchetti</h1>
      <p class="person__credentials">Clinical Psychologist BPsych,<br>BPsych (Hons),<br>MPsych (Clin),<br>MAPS</p>
    </div>

    <ul class="contact">
      <li>0439627015</li>
      <li>08 73615204</li>
      <li>hello@brightwatertelehealthcounselling.com.au</li>
      <li>brightwatertelehealthcounselling.com.au</li>
    </ul>
  </section>
</main>
</body>
</html>
```